Clinical Layout Builders - Stationery
Biz Cards + Stationary
Clinical Layout Builders - Stationery - Information Technology
Creative Brief
Professional
Dr. Elena M. Castillo
Director of Content Development
Ceiba Business Plaza #3, Suite 118 San Juan, PR 00941
(787) PENDING
elena.castillo@hnvwqbt.com
www.hnvwqbt.com
Need a second set of cards for: Dr. Luis F. Beltran Business Development Director Same info- address, fax and phone (Pending) Cell: (787) 555-0192 Email: luis.beltran@hnvwqbt.com
Either the logo, the website or something else. Feel free to be creative!

```html
<!DOCTYPE html>
<html lang="en">
<head>
<meta charset="utf-8">
<title>Clinical Layout Builders – Business Cards</title>
<link rel="stylesheet" href="https://fonts.googleapis.com/css2?family=Roboto:wght@300;400;500;700&display=swap">
<style>
  :root {
    --page: #efece6;
    --card-black: #0d0d0f;
    --card-grey: #3a3a3e;
    --magenta: #c2177f;
    --magenta-light: #e04aa6;
    --magenta-dark: #7a0e52;
    --ink-light: #d9d9dc;
    --ink-mid: #9a9aa0;
    --ink-dark: #2a0a1e;
  }
  * { margin: 0; padding: 0; box-sizing: border-box; }
  html, body {
    width: 1200px; height: 463px; overflow: hidden;
    background: var(--page);
    font-family: "Roboto", Arial, sans-serif;
  }
  .stage { position: relative; width: 1200px; height: 463px; }

  .card {
    position: absolute;
    width: 360px; height: 220px;
    border-radius: 14px;
    overflow: hidden;
    box-shadow: 0 6px 14px rgba(0,0,0,0.28);
  }
  .card--contact { left: 30px; top: 122px; background: var(--card-black); }
  .card--brand-dark {
    left: 420px; top: 122px;
    background: radial-gradient(ellipse at 50% 45%, #55555a 0%, #222226 45%, var(--card-black) 80%);
  }
  .card--brand-pink {
    left: 810px; top: 122px;
    background: radial-gradient(ellipse at 45% 40%, var(--magenta-light) 0%, var(--magenta) 50%, var(--magenta-dark) 100%);
  }

  /* contact card */
  .top-band { position: absolute; left: 0; top: 0; width: 360px; height: 80px; }
  .band-web {
    position: absolute; left: 96px; top: 18px;
    font-size: 8px; color: #fff; letter-spacing: 0.3px;
  }
  .contact-mark {
    position: absolute; right: 18px; top: 44px;
    display: flex; align-items: center; gap: 6px;
    font-size: 11px; font-weight: 500; color: var(--ink-light);
  }
  .contact-mark .dot { width: 8px; height: 8px; border-radius: 50%; background: var(--magenta); }
  .details {
    position: absolute; left: 14px; top: 128px;
    font-size: 7px; line-height: 10px; color: var(--ink-mid);
  }
  .details .row { display: flex; align-items: center; gap: 5px; }
  .details .bullet { width: 4px; height: 4px; border-radius: 50%; background: var(--magenta); }
  .person { position: absolute; left: 196px; top: 160px; }
  .person .name { font-size: 11px; font-weight: 500; color: var(--magenta-light); }
  .person .role { font-size: 7px; color: var(--ink-mid); margin-top: 2px; }

  /* brand cards */
  .brand {
    position: absolute; left: 0; right: 0; top: 82px;
    text-align: center;
  }
  .brand .tagline { font-size: 6px; letter-spacing: 1.6px; text-transform: uppercase; margin-bottom: 6px; }
  .brand .wordmark { font-size: 22px; font-weight: 700; letter-spacing: 0.5px; }
  .card--brand-dark .tagline { color: var(--ink-mid); }
  .card--brand-dark .wordmark { color: var(--magenta); }
  .card--brand-pink .tagline { color: #f6c6e3; }
  .card--brand-pink .wordmark { color: var(--ink-dark); }
</style>
</head>
<body>
<main class="stage">

  <section class="card card--contact" aria-label="Contact card">
    <svg class="top-band" viewBox="0 0 360 80" aria-hidden="true">
      <defs>
        <linearGradient id="bandFill" x1="0" y1="0" x2="1" y2="0">
          <stop offset="0" stop-color="#5a0a3c"/>
          <stop offset="0.5" stop-color="#c2177f"/>
          <stop offset="1" stop-color="#e04aa6"/>
        </linearGradient>
      </defs>
      <path d="M0 0 H360 V18 C250 14 120 26 0 52 Z" fill="url(#bandFill)"/>
      <path d="M0 52 C120 26 250 14 360 18" fill="none" stroke="#f08ac6" stroke-width="1"/>
    </svg>
    <div class="band-web">www.hnvwqbt.com</div>
    <div class="contact-mark"><span class="dot"></span>Clinical Layout Builders</div>

    <div class="details">
      <div>Ceiba Business Plaza #3, Suite 118</div>
      <div>San Juan, PR 00941</div>
      <div style="height:6px"></div>
      <div class="row"><span class="bullet"></span>T. (787) 555-0147</div>
      <div class="row"><span class="bullet"></span>F. (787) 555-0148</div>
      <div class="row"><span class="bullet"></span>elena.castillo@hnvwqbt.com</div>
    </div>

    <div class="person">
      <div class="name">Dr. Elena M. Castillo</div>
      <div class="role">Director of Content Development</div>
    </div>
  </section>

  <section class="card card--brand-dark" aria-label="Brand card, dark">
    <div class="brand">
      <div class="tagline">Clinical Layout Solutions</div>
      <div class="wordmark">Clinical Layout Builders</div>
    </div>
  </section>

  <section class="card card--brand-pink" aria-label="Brand card, magenta">
    <div class="brand">
      <div class="tagline">Clinical Layout Solutions</div>
      <div class="wordmark">Clinical Layout Builders</div>
    </div>
  </section>

</main>
</body>
</html>
```